Newsletter for customers of the IT company

Our company develops the software.
We need to create a monthly newsletter for our customers. The newsletter is distributed by email. Important points to follow:
1/ Newsletter has to include the logo and link to NetPeople profile of company - https://www.netpeople-hub.example/company/voret-systems-cz/?viewAsMember=true
2/ Corporate color is RGB #003265, you can use it.
3/ Use the most used fonts (calibri, times, trebuchet, verdana, ubuntu etc.).
4/ We need it in the html in final version.
5/ We would like to highlight the offer of webinars (3-4 per month).
6/ There have to be the space for news from company (2-3 per month) and link to website with news in the version of software.
7/ Space for contact.

```html
<!DOCTYPE html>
<html lang="en">
<head>
<meta charset="utf-8">
<title>VORET Newsletter</title>
<link href="https://fonts.googleapis.com/css2?family=Noto+Sans:wght@400;700&display=swap" rel="stylesheet">
<style>
:root{
  --brand:#003265;
  --ink:#333333;
  --muted:#555555;
  --white:#ffffff;
  --rule:#4d6f93;
}
*{margin:0;padding:0;box-sizing:border-box}
html,body{width:1200px;height:2751px;overflow:hidden;background:var(--white)}
body{position:relative;font-family:"Noto Sans",Verdana,sans-serif;color:var(--ink)}
a{color:inherit;text-decoration:none}
.abs{position:absolute}

.brand-mark{display:flex;align-items:center;gap:12px;font-weight:700;letter-spacing:1px}
.brand-mark .square{width:34px;height:34px;background:currentColor}
.header-logo{left:52px;top:26px;color:var(--brand);font-size:44px}
.social-link{right:60px;top:36px;font-size:26px;font-weight:700;color:var(--brand)}

.hero{left:0;top:104px;width:1200px;height:454px;
  background:radial-gradient(circle at 65% 45%,#6a5cf0 0%,#3b2f9a 30%,#22145a 60%,#1a0d3c 100%)}

.section-title{font-size:48px;font-weight:400;color:var(--brand)}
.webinars-title{left:60px;top:624px}
.intro{left:67px;top:704px;width:1062px;font-size:19px;line-height:39px;text-align:justify;color:#222}

.col-label{font-size:22px;font-weight:700;color:var(--muted);top:854px}
.panel{background:var(--brand)}
.training-panel{left:69px;top:902px;width:358px;height:451px}
.place-panel{left:777px;top:902px;width:358px;height:451px}
.topic-list{left:428px;top:902px;width:334px;height:451px;background:var(--white);box-shadow:0 0 8px rgba(0,0,0,.18);padding:34px 0 0 10px;list-style:none}
.topic-list li{font-size:15px;line-height:33px;padding-left:20px;position:relative;color:#333}
.topic-list li::before{content:"";position:absolute;left:2px;top:12px;width:8px;height:8px;border:2px solid #8aa3bf;transform:rotate(45deg)}
.topic-list .wrap{line-height:33px}

.course{position:absolute;left:12px;width:336px;height:49px;background:var(--white);color:#222;font-size:19px;line-height:49px;padding-left:10px;white-space:nowrap}
.course.active,.venue.active{background:var(--brand);color:var(--white);border:2px solid var(--white);line-height:45px}
.venue{position:absolute;left:13px;width:212px;height:49px;background:var(--white);color:#222;font-size:19px;line-height:49px;padding-left:12px}
.date{position:absolute;left:238px;color:var(--white);font-size:19px;line-height:49px}
.chevron{position:absolute;bottom:14px}

.news-title{left:70px;top:1440px}
.news-tag{font-size:20px;font-weight:700;color:#333}
.news-date{font-size:21px;color:#444;text-align:right;width:200px}
.news-head{font-size:21px;font-weight:700;color:#333;line-height:39px;width:660px}
.news-body{font-size:22px;line-height:39px;color:#444;width:657px;text-align:justify}
.photo{border-radius:2px}

.footer{left:0;top:2313px;width:1200px;height:438px;background:var(--brand)}
.footer-logo{left:0;width:1200px;top:2360px;justify-content:center;color:var(--white);font-size:60px}
.contact{display:flex;align-items:center;gap:16px;color:var(--white);font-size:22px;line-height:39px}
.icon{width:48px;height:48px;border-radius:50%;background:var(--white);display:flex;align-items:center;justify-content:center;flex:none}
.footer-rule{left:0;top:2673px;width:1200px;height:1px;background:var(--rule)}
.copyright{left:0;width:1200px;top:2696px;text-align:center;color:var(--white);font-size:19px}
</style>
</head>
<body>

<header>
  <div class="abs brand-mark header-logo"><span class="square"></span>VORET</div>
  <a class="abs social-link" href="https://www.netpeople-hub.example/company/voret-systems-cz/?viewAsMember=true">NetPeople</a>
</header>

<div class="abs hero" role="img" aria-label="Illustration of a glowing laptop with floating data dashboards and charts"></div>

<section class="webinars">
  <h2 class="abs section-title webinars-title">Webinars</h2>
  <p class="abs intro">The training takes place via the MeetLine Rooms application. We will send registered participants an invitation with instructions to join the day before the training. To participate in the training, you need a computer connected to the Internet.</p>

  <div class="abs col-label" style="left:72px">Training</div>
  <div class="abs col-label" style="left:780px">Place</div>

  <div class="abs panel training-panel">
    <div class="course" style="top:20px">ORBIS4 Wages - special for schools</div>
    <div class="course" style="top:83px">ORBIS4 - filters, views, user reports</div>
    <div class="course" style="top:148px">ORBIS4 Wages - non-employment</div>
    <div class="course active" style="top:215px">ORBIS4 Income agendas - inventory</div>
    <div class="course" style="top:283px">ORBIS4 Income agendas - billing</div>
    <div class="course" style="top:347px">ORBIS4 Register for beginners</div>
    <svg class="chevron" style="left:312px" width="26" height="22" viewBox="0 0 26 22" fill="none" stroke="#fff" stroke-width="2"><path d="M3 3l10 8 10-8M3 11l10 8 10-8"/></svg>
  </div>

  <ul class="abs topic-list">
    <li>Legislative changes for 2024</li>
    <li>Setting up personal cards and work<br>relationships</li>
    <li>Pay scales</li>
    <li>Direct and indirect pedagogical activity</li>
    <li>Supplements for direct teaching activity<br>above the scope</li>
    <li>Teacher self-study</li>
    <li>FKSP</li>
    <li>Statement P1-04 and P1c-01</li>
    <li>The most common errors in payroll<br>processing</li>
  </ul>

  <div class="abs panel place-panel">
    <div class="venue" style="top:20px">Online Webinar</div><div class="date" style="top:20px">23/02/2024</div>
    <div class="venue" style="top:83px">Online Webinar</div><div class="date" style="top:83px">16/02/2024</div>
    <div class="venue" style="top:146px">Online Webinar</div><div class="date" style="top:146px">15/02/2024</div>
    <div class="venue active" style="top:211px">Online Webinar</div><div class="date" style="top:211px">02/09/2024</div>
    <div class="venue" style="top:281px">Online Webinar</div><div class="date" style="top:281px">30/01/2024</div>
    <div class="venue" style="top:347px">Online Webinar</div><div class="date" style="top:347px">18/01/2024</div>
    <svg class="chevron" style="left:310px" width="26" height="22" viewBox="0 0 26 22" fill="none" stroke="#fff" stroke-width="2"><path d="M3 3l10 8 10-8M3 11l10 8 10-8"/></svg>
  </div>
</section>

<section class="news">
  <h2 class="abs section-title news-title">News</h2>

  <article>
    <div class="abs news-tag" style="left:72px;top:1523px">ORBIS4</div>
    <div class="abs news-date" style="left:919px;top:1527px">27/11/2023</div>
    <h3 class="abs news-head" style="left:70px;top:1568px">Automatic logout when the user is inactive</h3>
    <p class="abs news-body" style="left:72px;top:1623px">Requirements for the security of information systems are constantly increasing in proportion to the growth of threats in cyberspace. Next year, the ORBIS4 information system will become a regulated service under the new cyber security law and will have to meet a number of security requirements defined in the decrees.</p>
    <div class="abs photo" style="left:748px;top:1572px;width:401px;height:290px;background:linear-gradient(135deg,#5a4a3a 0%,#b88a5a 40%,#d9c9b5 70%,#6b5a4c 100%)" role="img" aria-label="Photo of three colleagues reviewing work on a laptop in an office"></div>
  </article>

  <article>
    <div class="abs news-tag" style="left:72px;top:1903px">ORBIS4</div>
    <div class="abs news-date" style="left:919px;top:1907px">27/11/2023</div>
    <h3 class="abs news-head" style="left:70px;top:1948px">ORBIS4 update: Increased security with automatic client session expiration</h3>
    <p class="abs news-body" style="left:72px;top:2038px">As threats in cyberspace increase, the security of our software becomes our top priority. As part of the upcoming ORBIS4 update, we have implemented a new security function - automatic expiration of client sessions (session expiration in Czech), i.e. automatic logout during inactivity.</p>
    <div class="abs photo" style="left:747px;top:1944px;width:403px;height:297px;background:linear-gradient(180deg,#ececec 0%,#dcdcdc 55%,#b9c3cf 80%,#e8e8e8 100%)" role="img" aria-label="Photo of a business team meeting around a table with laptops"></div>
  </article>
</section>

<footer>
  <div class="abs footer"></div>
  <div class="abs brand-mark footer-logo"><span class="square" style="width:46px;height:46px"></span>VORET</div>

  <div class="abs contact" style="left:99px;top:2547px">
    <span class="icon"><svg width="24" height="24" viewBox="0 0 24 24"><path fill="#003265" d="M6.6 10.8a15 15 0 0 0 6.6 6.6l2.2-2.2c.3-.3.7-.4 1-.2 1.1.4 2.3.6 3.6.6.6 0 1 .4 1 1V20c0 .6-.4 1-1 1A17 17 0 0 1 3 4c0-.6.4-1 1-1h3.5c.6 0 1 .4 1 1 0 1.3.2 2.5.6 3.6.1.3 0 .7-.2 1z"/></svg></span>
    <span>415 603 270</span>
  </div>
  <div class="abs contact" style="left:384px;top:2547px">
    <span class="icon"><svg width="26" height="20" viewBox="0 0 26 20" fill="none" stroke="#003265" stroke-width="2"><rect x="2" y="2" width="22" height="16" rx="2"/><path d="M2 3l11 9 11-9M2 17l8-7M24 17l-8-7"/></svg></span>
    <a href="mailto:podpora@voret.example">podpora@voret.example</a>
  </div>
  <div class="abs contact" style="left:717px;top:2547px;align-items:flex-start">
    <span class="icon"><svg width="22" height="28" viewBox="0 0 22 28"><path fill="#003265" d="M11 1C5.5 1 1 5.4 1 10.8 1 18 11 27 11 27s10-9 10-16.2C21 5.4 16.5 1 11 1zm0 14a4 4 0 1 1 0-8 4 4 0 0 1 0 8z"/></svg></span>
    <span>VORET spol. s.r.o, Lipová 214<br>Nové Lipno 471 09</span>
  </div>

  <div class="abs footer-rule"></div>
  <div class="abs copyright">© Copyrights 2023 VORET.All rights reserved</div>
</footer>

</body>
</html>
```